Banner ad to encourage people to complete a survey

This is a banner ad which will be posted on www.veltrona.org. The goal of the add is to encourage people to click on it and take the survey.
File Format: Standard .jpg image (no Flash)
Ad dimension (Pixels): 300w x 250d
Max File Size: 24k
- Use a border to differentiate the banner from page content (page background is white)
- No transparent backgrounds
Ad Message: "Speech-Language Pathologist Survey"
Additional text: "Please take two minutes to complete a survey on the future of work patterns for Speech-Language Pathologists and enter a draw to win an Zorbik"
Target Market(s)
The respondents are professional and well educated and the ad/colour scheme should reflect this.
Font styles to use
Colors
Designer to choose colors to be used in the design.
Look and feel

```html
<!DOCTYPE html>
<html lang="en">
<head>
<meta charset="utf-8">
<title>Speech-Language Pathologist Survey Banner</title>
<link rel="stylesheet" href="https://fonts.googleapis.com/css2?family=Roboto+Condensed:wght@700;800&display=swap">
<style>
  :root {
    --page-bg: #0f6c91;
    --banner-bg: #ffffff;
    --title-blue: #1b6f9c;
    --band-top: #33b0e0;
    --band-bottom: #1c6f99;
    --band-text: #ffffff;
    --prize-yellow: #f8b417;
    --people-a: #f4b321;
    --people-b: #e4127f;
    --people-c: #5b5f66;
    --people-d: #2aa6dc;
    --burst: #f6c431;
    --tablet: #e9eef2;
  }
  * { box-sizing: border-box; margin: 0; padding: 0; }
  html, body {
    width: 1200px;
    height: 1143px;
    overflow: hidden;
    background: var(--page-bg);
  }
  .banner {
    position: absolute;
    left: 350px;
    top: 298px;
    width: 520px;
    height: 433px;
    background: var(--banner-bg);
    overflow: hidden;
    box-shadow: 0 10px 30px rgba(0, 0, 0, 0.35);
    font-family: "Roboto Condensed", "Arial Narrow", sans-serif;
  }
  .banner-title {
    position: absolute;
    left: 0;
    top: 10px;
    width: 100%;
    padding-left: 20px;
    text-align: center;
    color: var(--title-blue);
    font-weight: 800;
    text-transform: uppercase;
    line-height: 1;
  }
  .banner-title .line-one {
    display: block;
    font-size: 43px;
  }
  .banner-title .line-two {
    display: block;
    font-size: 36px;
    margin-top: 3px;
  }
  .people-illustration {
    position: absolute;
    left: 70px;
    top: 100px;
    width: 392px;
    height: 208px;
    border-radius: 90px 90px 0 0;
    background:
      radial-gradient(ellipse at 50% 25%, rgba(228, 18, 127, 0.8) 0 20%, transparent 40%),
      linear-gradient(90deg, var(--people-a) 0%, var(--people-b) 25%, var(--people-c) 50%, var(--people-a) 72%, var(--people-c) 86%, var(--people-d) 100%);
    opacity: 0.85;
  }
  .info-band {
    position: absolute;
    left: 0;
    top: 308px;
    width: 100%;
    height: 125px;
    background: linear-gradient(180deg, var(--band-top) 0%, var(--band-top) 35%, var(--band-bottom) 100%);
  }
  .info-text {
    position: absolute;
    right: 180px;
    top: 8px;
    width: 340px;
    text-align: right;
    color: var(--band-text);
    font-weight: 700;
    font-size: 19px;
    line-height: 24px;
  }
  .info-text .prize {
    color: var(--prize-yellow);
    font-weight: 800;
    font-size: 31px;
    text-transform: uppercase;
    line-height: 30px;
    vertical-align: -2px;
  }
  .tablet-illustration {
    position: absolute;
    left: 354px;
    top: 262px;
    width: 160px;
    height: 162px;
    background: radial-gradient(closest-side, var(--tablet) 0 55%, var(--burst) 57% 98%, transparent 100%);
  }
</style>
</head>
<body>
  <main class="banner">
    <h1 class="banner-title">
      <span class="line-one">Speech-Language</span>
      <span class="line-two">Pathologist Survey</span>
    </h1>
    <div class="people-illustration" role="img" aria-label="Colourful silhouettes of people in a row with overlapping speech bubbles above them"></div>
    <section class="info-band">
      <p class="info-text">
        Please take two minutes to complete a<br>
        survey on the future of work patterns for<br>
        Speech-Language Pathologists and<br>
        enter a draw to <span class="prize">Win an Zorbik</span>
      </p>
    </section>
    <div class="tablet-illustration" role="img" aria-label="Tablet computer on a yellow starburst, the prize to be won"></div>
  </main>
</body>
</html>
```